Powerpoint for Travio

Check out the attached sample powerpoint, we would like our powerpoint to look similar to this. in the slides where you see monitor, we would like to put pics of different industries in each monitor. like images of hotels, hospitals, large business with multiple locations, small business, retail)

The Powerpoint will contain the below slides

About US
Our Guarantee – 100% satisfaction and 30% cost savings
Products & Services ( Hosted PBX phone system, SIP Trunking, Network security solutions, commercial grade band width and firewalls, IT Network design services)
Features ( One slide for this we will enter the content)
Industries ( Small business, hospitality, hospitals, Banks for secure voice, Large business with multiple locations, Retail)
Hosted PBX
Why Travio
Channel partners
Our customers
Contact us
Updates

Target Market(s)

Small business, hospitality, hospitals, Banks for secure voice, Large business with multiple locations, Retail, law firms, insurance companies

Industry/Entity Type

Security

Requirements
Must have
• Please look at the attached powerpoint for color, style, font details

```html
<!DOCTYPE html>
<html lang="en">
<head>
<meta charset="utf-8">
<title>Travio – Cloud Communication Presentation</title>
<link href="https://fonts.googleapis.com/css2?family=Open+Sans:wght@400;600;700&display=swap" rel="stylesheet">
<style>
  :root {
    --canvas: #e4e4e4;
    --slide-top: #ffffff;
    --slide-body-a: #f7f7f7;
    --slide-body-b: #e6e6e6;
    --ink: #333333;
    --ink-soft: #444444;
    --ink-muted: #555555;
    --brand-blue: #1b9ad8;
    --orange: #ef7d1a;
    --green: #9cc31c;
    --sky: #1a9fe0;
    --magenta: #e0127c;
    --yellow: #f5d90a;
    --red: #e52a2a;
    --navy: #1f4e8c;
  }
  * { box-sizing: border-box; margin: 0; padding: 0; }
  html, body { width: 1200px; height: 900px; overflow: hidden; }
  body {
    background: var(--canvas);
    font-family: "Open Sans", Arial, sans-serif;
    color: var(--ink);
    position: relative;
  }
  .slide {
    position: absolute;
    width: 583px;
    height: 436px;
    background: linear-gradient(180deg, var(--slide-body-a) 0%, var(--slide-body-b) 100%);
    box-shadow: 0 1px 3px rgba(0,0,0,0.25);
    overflow: hidden;
  }
  .slide::before {
    content: "";
    position: absolute; left: 0; top: 0; right: 0;
    height: 30px;
    background: var(--slide-top);
  }
  .slide-footer {
    position: absolute; left: 0; right: 0; bottom: 0;
    height: 44px;
    background: var(--slide-top);
  }
  .page-number {
    position: absolute; left: 22px; top: 19px;
    font-size: 7px; color: var(--ink-muted);
  }
  .footer-brand {
    position: absolute; right: 22px; top: 14px;
    font-size: 11px; font-weight: 600; color: var(--ink-soft);
    display: flex; align-items: center; gap: 4px;
    letter-spacing: 0.3px;
  }
  .footer-brand .brand-dot {
    width: 8px; height: 8px; background: var(--brand-blue);
  }
  .slide--cover { left: 10px; top: 12px; }
  .slide--about { left: 606px; top: 12px; }
  .slide--products { left: 10px; top: 458px; }
  .slide--features { left: 606px; top: 458px; }

  .slide-title {
    position: absolute; left: 40px; top: 38px;
    font-size: 27px; font-weight: 400; color: var(--ink);
    letter-spacing: 0.3px;
  }

  /* Cover */
  .cover-brand {
    position: absolute; left: 104px; top: 190px;
    font-size: 34px; font-weight: 600; color: var(--brand-blue);
  }
  .cover-title {
    position: absolute; left: 252px; top: 164px;
    font-size: 28px; line-height: 40px; color: var(--ink-muted);
  }
  .cover-url {
    position: absolute; left: 253px; top: 252px;
    font-size: 12px; letter-spacing: 3.2px; color: var(--ink-muted);
  }

  /* About */
  .about-text {
    position: absolute; left: 40px; top: 80px; width: 300px;
    font-size: 9.5px; line-height: 19px; color: var(--ink);
  }
  .stat { position: absolute; left: 64px; color: var(--ink-soft); }
  .stat-value { font-size: 42px; font-weight: 700; line-height: 46px; }
  .stat-label { font-size: 19px; line-height: 24px; }
  .stat--satisfaction { top: 182px; }
  .stat--savings { top: 284px; }
  .stat--savings .stat-value { letter-spacing: 4px; }
  .bubble-cloud {
    position: absolute; left: 266px; top: 84px;
    width: 310px; height: 310px;
  }
  .bubble-stat {
    position: absolute; text-align: center; color: var(--ink);
    border-radius: 50%;
    display: flex; flex-direction: column; justify-content: center; align-items: center;
  }
  .bubble-stat strong { font-size: 22px; font-weight: 700; line-height: 24px; }
  .bubble-stat span { font-size: 11.5px; line-height: 14px; }
  .bubble-stat--projects { left: 396px; top: 98px; width: 120px; height: 94px; background: var(--orange); }
  .bubble-stat--clients { left: 296px; top: 160px; width: 116px; height: 100px; background: var(--green); }
  .bubble-stat--pros { left: 384px; top: 272px; width: 94px; height: 80px; background: var(--sky); }

  /* Products */
  .products-text {
    position: absolute; left: 40px; top: 80px; width: 486px;
    font-size: 9.6px; line-height: 14px; color: var(--ink);
  }
  .service {
    position: absolute; top: 176px; width: 130px;
    text-align: center; font-size: 9.5px; line-height: 13px; color: var(--ink);
  }
  .service svg { display: block; margin: 0 auto 24px; width: 92px; height: 90px; }
  .service small { display: block; font-size: 8px; line-height: 11px; }
  .service--pbx { left: 15px; }
  .service--sip { left: 138px; }
  .service--security { left: 280px; }
  .service--design { left: 430px; }

  /* Features */
  .feature-list {
    position: absolute; left: 40px; top: 79px; width: 480px;
    list-style: none; font-size: 9.5px; line-height: 15px; color: var(--ink);
  }
  .feature-list li { position: relative; padding-left: 12px; }
  .feature-list li::before {
    content: ""; position: absolute; left: 1px; top: 6px;
    width: 3px; height: 3px; border-radius: 50%; background: var(--brand-blue);
  }
</style>
</head>
<body>

<section class="slide slide--cover">
  <div class="cover-brand">Travio</div>
  <h1 class="cover-title">Cloud<br>Communication</h1>
  <div class="cover-url">travio.com</div>
</section>

<section class="slide slide--about">
  <h2 class="slide-title">ABOUT US</h2>
  <p class="about-text">Travio is a cloud communication company, our specialization embraces the complete range of services in VOIP, hosted PBX, technical support and maintenance.</p>
  <div class="stat stat--satisfaction">
    <div class="stat-value">100%</div>
    <div class="stat-label">satisfaction</div>
  </div>
  <div class="stat stat--savings">
    <div class="stat-value">30%</div>
    <div class="stat-label">cost savings</div>
  </div>
  <div class="bubble-cloud" role="img" aria-label="Round cluster of many small colourful speech bubbles"
       style="border-radius:50%;background:radial-gradient(circle at 50% 50%, rgba(26,159,224,0.35) 0%, rgba(224,18,124,0.3) 35%, rgba(156,195,28,0.3) 60%, rgba(239,125,26,0.25) 80%, rgba(245,217,10,0) 100%);"></div>
  <div class="bubble-stat bubble-stat--projects"><strong>900+</strong><span>completed<br>projects</span></div>
  <div class="bubble-stat bubble-stat--clients"><strong>500+</strong><span>clients</span></div>
  <div class="bubble-stat bubble-stat--pros"><strong>100+</strong><span>pros</span></div>
  <footer class="slide-footer">
    <span class="page-number">Page 2</span>
    <span class="footer-brand"><i class="brand-dot"></i>Travio</span>
  </footer>
</section>

<section class="slide slide--products">
  <h2 class="slide-title">PRODUCTS &amp; SERVICES</h2>
  <p class="products-text">Travio is one of the leaders in the domain of web design and development offering the entire range of services required for the successful implementation of web and mobile-based solutions of any complexity from an idea to the launch. We employ our qualified resources, know-how and cutting edge industry tools to achieve our main goal of creating high quality products within the agreed time period.</p>

  <div class="service service--pbx">
    <svg viewBox="0 0 92 90" aria-hidden="true">
      <rect x="6" y="12" width="42" height="76" rx="5" fill="var(--brand-blue)"/>
      <rect x="12" y="20" width="30" height="30" fill="#fff"/>
      <g fill="#fff">
        <rect x="14" y="60" width="6" height="5"/><rect x="24" y="60" width="6" height="5"/><rect x="34" y="60" width="6" height="5"/>
        <rect x="14" y="70" width="6" height="5"/><rect x="24" y="70" width="6" height="5"/><rect x="34" y="70" width="6" height="5"/>
      </g>
      <path d="M22 50 C22 30 38 18 62 18 L62 6 L86 24 L62 42 L62 30 C46 30 34 36 22 50 Z" fill="var(--brand-blue)" stroke="#f2f2f2" stroke-width="3"/>
    </svg>
    Hosted PBX phone<br>system
  </div>

  <div class="service service--sip">
    <svg viewBox="0 0 92 90" aria-hidden="true">
      <path d="M24 58 C10 58 6 48 8 40 C10 32 18 28 24 30 C26 16 38 8 50 10 C62 12 68 20 70 28 C80 28 88 36 86 46 C84 54 78 58 70 58 Z"
            fill="none" stroke="var(--brand-blue)" stroke-width="8" stroke-linejoin="round"/>
      <g fill="var(--brand-blue)">
        <rect x="44" y="58" width="4" height="14"/>
        <rect x="16" y="72" width="60" height="4"/>
        <rect x="14" y="78" width="14" height="8"/><rect x="39" y="78" width="14" height="8"/><rect x="64" y="78" width="14" height="8"/>
      </g>
    </svg>
    SIP Trunking
  </div>

  <div class="service service--security">
    <svg viewBox="0 0 92 90" aria-hidden="true">
      <g stroke="var(--brand-blue)" stroke-width="5" stroke-linecap="round">
        <line x1="42" y1="42" x2="42" y2="8"/><line x1="42" y1="42" x2="12" y2="22"/>
        <line x1="42" y1="42" x2="8" y2="50"/><line x1="42" y1="42" x2="22" y2="76"/>
        <line x1="42" y1="42" x2="72" y2="16"/><line x1="42" y1="42" x2="80" y2="40"/>
      </g>
      <g fill="var(--brand-blue)">
        <circle cx="42" cy="42" r="16"/>
        <circle cx="42" cy="8" r="6"/><circle cx="12" cy="22" r="6"/><circle cx="8" cy="50" r="6"/>
        <circle cx="22" cy="76" r="6"/><circle cx="72" cy="16" r="6"/><circle cx="80" cy="40" r="6"/>
        <circle cx="66" cy="66" r="19" stroke="#f2f2f2" stroke-width="3"/>
      </g>
      <path d="M57 66 L64 73 L76 60" fill="none" stroke="#fff" stroke-width="5" stroke-linecap="round" stroke-linejoin="round"/>
    </svg>
    Network security solutions
    <small>Commercial grade<br>band width and firewalls</small>
  </div>

  <div class="service service--design">
    <svg viewBox="0 0 92 90" aria-hidden="true">
      <rect x="4" y="8" width="84" height="70" rx="6" fill="none" stroke="var(--brand-blue)" stroke-width="7"/>
      <path d="M50 44 C50 40 56 40 56 44 L56 56 L60 54 C62 53 66 54 66 57 L70 56 C72 56 76 57 76 60 L78 60 C80 60 84 62 84 66 L84 76 C84 82 80 86 74 86 L62 86 C58 86 54 82 52 78 L44 66 C42 62 46 58 50 62 Z"
            fill="var(--brand-blue)" stroke="#f2f2f2" stroke-width="2.5"/>
    </svg>
    IT Network design<br>services
  </div>

  <footer class="slide-footer">
    <span class="page-number">Page 3</span>
    <span class="footer-brand"><i class="brand-dot"></i>Travio</span>
  </footer>
</section>

<section class="slide slide--features">
  <h2 class="slide-title">FEATURES</h2>
  <ul class="feature-list">
    <li>This is a dummy text.<br>Please ignore the following content as it is dummy text.</li>
    <li>This is definitely some dummy text.</li>
    <li>The text here is meaningless as it is used to fill this slide.</li>
  </ul>
  <footer class="slide-footer">
    <span class="page-number">Page 4</span>
    <span class="footer-brand"><i class="brand-dot"></i>Travio</span>
  </footer>
</section>

</body>
</html>
```